Redesign of Plastic Surgeon Website to fully responsive / modern feel

Hi

Our current website is out of date www.harbourlinecosmetic.org

We want a fresh / modern looking design
Needs to be fully responsive design that works extremely well on ipad and mobile device

Would like design for both full screen website and mobile

Have listed a few websites of other plastic surgeons we like
http://www.reformclinicdaily.com/
http://www.peterholtbymd.com/
http://www.corvanbeauty.com/
http://www.tidewellcontouring.com/

Menu needs to include
1. About Us
2. Procedures (see current website for example)
3. News
4. Patient Resources
5. Contact Us

We are flexible with colours / images / layout

I have uploaded a document that has some content - the face pages content is completed only

some of the procedures can have content upwards of 4000 words - total website can be large with over 40,000 words
Updates

Target Market(s)

Mainly women 20-60 85% of practice
Some men 15%

Industry/Entity Type

Plastic Surgery

Number of Pages Required

5+ page

Requirements
Must have
• We need designs for
• Homepage
• Internal pages
• 1. Landing pages for breast / body / face / non surgical main pages
• 2. Procedure pages for individual pages under each section - eg breast augmentation
• 3. About us pages - like meet the doctor, our staff, clinics
• 4. Contact page
• 5. Blog / News page
Nice to have
• See our list of websites for examples of designs we like
• Like full screen design with nice hero image
• Needs to have good to call to action messages on home page like
• Specials, procedure of the month, etc

```html
<!DOCTYPE html>
<html lang="en">
<head>
<meta charset="utf-8">
<title>Harbourline Cosmetic Institute — Homepage</title>
<link rel="stylesheet" href="https://fonts.googleapis.com/css2?family=PT+Sans:wght@400;700&family=PT+Serif:ital,wght@0,400;0,700;1,400&display=swap">
<style>
  :root {
    --stage: #e4e4e4;
    --white: #ffffff;
    --ink: #1e1e1e;
    --ink-soft: #5a5a5a;
    --muted: #9a9a9a;
    --charcoal: #2a2a2a;
    --charcoal-deep: #1c1c1c;
    --charcoal-line: #3d3d3d;
    --tile-grey: #4a4a4a;
    --button: #2f2f2f;
    --serif: "PT Serif", Georgia, serif;
    --sans: "PT Sans", Arial, sans-serif;
  }
  * { box-sizing: border-box; margin: 0; padding: 0; }
  html, body { width: 1200px; height: 600px; overflow: hidden; }
  body { background: var(--stage); font-family: var(--sans); color: var(--ink); position: relative; }

  .page { position: absolute; top: 40px; width: 560px; height: 520px; overflow: hidden; box-shadow: 0 6px 18px rgba(0,0,0,.18); }
  .page--top { left: 30px; background: var(--white); }
  .page--content { left: 610px; background: var(--charcoal); color: #cfcfcf; }

  /* Header */
  .site-header { height: 104px; background: var(--charcoal); position: relative; }
  .site-header::before { content: ""; position: absolute; left: 0; right: 0; top: 8px; height: 1px; background: #555; }
  .brand { position: absolute; left: 28px; top: 20px; display: flex; align-items: center; gap: 8px; }
  .brand__mark { width: 10px; height: 10px; background: var(--white); }
  .brand__name { font-family: var(--serif); font-size: 12px; line-height: 15px; color: var(--white); text-transform: uppercase; letter-spacing: 1.5px; width: 120px; }
  .call { position: absolute; left: 180px; top: 26px; display: flex; align-items: center; gap: 8px; color: var(--white); font-size: 12px; }
  .call__icon { width: 20px; height: 20px; border-radius: 3px; background: var(--white); display: flex; align-items: center; justify-content: center; }
  .search { position: absolute; right: 40px; top: 24px; width: 110px; height: 18px; background: var(--white); border: 1px solid #999; font-size: 9px; color: var(--muted); padding: 3px 6px; }
  .main-nav { position: absolute; left: 180px; bottom: 14px; display: flex; gap: 14px; font-size: 11px; color: #bdbdbd; }
  .main-nav .is-active { color: var(--white); border-bottom: 1px solid var(--white); padding-bottom: 2px; }

  /* Hero */
  .hero { position: absolute; top: 104px; left: 0; right: 0; height: 356px; background: linear-gradient(90deg, #ffffff 0%, #f7f7f7 60%, #ececec 100%); }
  .hero__photo { position: absolute; right: 30px; top: 0; width: 210px; height: 356px; background: linear-gradient(180deg, #e9e9e9, #cfcfcf); }
  .hero__copy { position: absolute; left: 56px; top: 90px; width: 290px; }
  .hero__title { font-family: var(--serif); font-size: 21px; line-height: 26px; color: var(--ink); }
  .hero__lead { margin-top: 8px; font-size: 11px; color: var(--ink-soft); }
  .hero__text { margin-top: 6px; font-size: 8.5px; line-height: 12px; color: var(--muted); }
  .btn { margin-top: 14px; display: inline-flex; align-items: center; gap: 8px; background: var(--button); color: var(--white); font-size: 8px; letter-spacing: 1px; text-transform: uppercase; padding: 5px 10px 5px 5px; }
  .btn__tick { width: 12px; height: 12px; border-radius: 50%; background: var(--white); display: flex; align-items: center; justify-content: center; }
  .hero__arrow { position: absolute; top: 160px; width: 18px; height: 24px; background: #bdbdbd; display: flex; align-items: center; justify-content: center; }
  .hero__arrow--prev { left: 10px; }
  .hero__arrow--next { right: 10px; background: #555; }
  .strip { position: absolute; left: 0; right: 0; bottom: 0; height: 60px; background: var(--charcoal); }

  /* Content page */
  .features { display: flex; gap: 10px; padding: 20px 56px 0; }
  .feature { width: 142px; }
  .feature__photo { height: 84px; position: relative; background: linear-gradient(135deg, #5b5b5b, #8c8c8c); }
  .feature__label { position: absolute; left: 0; bottom: 0; width: 56px; height: 84px; background: rgba(40,40,40,.75); color: var(--white); font-family: var(--serif); font-size: 10px; letter-spacing: 1px; text-transform: uppercase; display: flex; align-items: flex-end; padding: 0 0 8px 8px; }
  .feature__text { margin-top: 8px; font-size: 7.5px; line-height: 10px; color: #aaa; }
  .feature__more { margin-top: 4px; text-align: right; font-size: 7.5px; color: var(--white); }

  .about { display: flex; gap: 26px; padding: 26px 56px 0; }
  .about__photo { width: 150px; height: 120px; background: linear-gradient(160deg, #3a3a3a, #6e6e6e); flex: none; }
  .about__title { font-size: 11px; font-weight: 700; color: var(--white); display: flex; align-items: center; gap: 8px; }
  .about__title::after { content: ""; flex: 1; height: 3px; background: #555; }
  .about__sub { font-family: var(--serif); font-style: italic; font-size: 10px; color: #ddd; margin: 4px 0 6px; }
  .about__text { font-size: 7.5px; line-height: 10.5px; color: #aaa; margin-bottom: 6px; }
  .dots { display: flex; gap: 4px; margin: 8px 0 0 110px; }
  .dots span { width: 5px; height: 5px; border-radius: 50%; background: #777; }
  .dots span:first-child { background: var(--white); }

  .site-footer { position: absolute; left: 0; right: 0; bottom: 0; height: 170px; background: var(--charcoal-deep); border-top: 1px solid var(--charcoal-line); padding: 16px 56px 0; }
  .footer-cols { display: flex; gap: 26px; }
  .footer-col h4 { font-size: 8px; color: var(--white); letter-spacing: .5px; margin-bottom: 5px; }
  .footer-col li { list-style: none; font-size: 7px; line-height: 10px; color: #999; }
  .footer-col--updates { width: 100px; }
  .footer-col--updates p { font-size: 7px; line-height: 9.5px; color: #999; margin-bottom: 5px; }
  .gallery-grid { display: grid; grid-template-columns: repeat(4, 14px); gap: 3px; }
  .gallery-grid span { width: 14px; height: 14px; background: linear-gradient(135deg, #555, #999); }
  .footer-bar { position: absolute; left: 0; right: 0; bottom: 0; height: 30px; border-top: 1px solid var(--charcoal-line); display: flex; align-items: center; justify-content: space-between; padding: 0 56px; font-size: 7px; color: #888; }
  .social { display: flex; gap: 6px; }
  .social span { width: 9px; height: 9px; border-radius: 50%; background: #777; }
</style>
</head>
<body>

<section class="page page--top">
  <header class="site-header">
    <div class="brand"><span class="brand__mark"></span><span class="brand__name">Harbourline Cosmetic Institute</span></div>
    <div class="call">
      <span class="call__icon"><svg width="11" height="11" viewBox="0 0 24 24"><path d="M6.6 10.8a15.1 15.1 0 0 0 6.6 6.6l2.2-2.2a1 1 0 0 1 1-.25 11.4 11.4 0 0 0 3.6.57 1 1 0 0 1 1 1V20a1 1 0 0 1-1 1A17 17 0 0 1 3 4a1 1 0 0 1 1-1h3.5a1 1 0 0 1 1 1c0 1.25.2 2.45.57 3.57a1 1 0 0 1-.25 1z" fill="#2a2a2a"/></svg></span>
      <span>Call for Appointments <strong>02 5550 1750</strong></span>
    </div>
    <div class="search">Search</div>
    <nav class="main-nav">
      <span class="is-active">Home</span><span>Practices</span><span>News</span><span>Gallery</span><span>Patient</span><span>Surgical Procedures</span><span>Contact Us</span>
    </nav>
  </header>
  <div class="hero">
    <div class="hero__photo" role="img" aria-label="Black and white photograph of a seated woman, hero image"></div>
    <div class="hero__copy">
      <h1 class="hero__title">Nurture your natural beauty with the rejuvenation you deserve...</h1>
      <p class="hero__lead">Invest in yourself, renew your look and refresh your confidence</p>
      <p class="hero__text">We provide exceptional quality of service in plastic and cosmetic surgery and improve the appearance, wellbeing and self confidence of clients entrusting us with their care.</p>
      <span class="btn"><span class="btn__tick"><svg width="8" height="8" viewBox="0 0 10 10"><path d="M1.5 5.2 4 7.5 8.5 2.5" fill="none" stroke="#2f2f2f" stroke-width="1.6"/></svg></span>Read More</span>
    </div>
    <span class="hero__arrow hero__arrow--prev"><svg width="6" height="10" viewBox="0 0 6 10"><path d="M5 1 1 5l4 4" fill="none" stroke="#fff" stroke-width="1.5"/></svg></span>
    <span class="hero__arrow hero__arrow--next"><svg width="6" height="10" viewBox="0 0 6 10"><path d="M1 1l4 4-4 4" fill="none" stroke="#fff" stroke-width="1.5"/></svg></span>
  </div>
  <div class="strip"></div>
</section>

<section class="page page--content">
  <div class="features">
    <article class="feature">
      <div class="feature__photo" role="img" aria-label="Black and white portrait photograph for face procedures"><span class="feature__label">Face</span></div>
      <p class="feature__text">Refined facial care tailored to you, from subtle lifts to complete renewal of your features.</p>
      <p class="feature__more">Learn More ›</p>
    </article>
    <article class="feature">
      <div class="feature__photo" role="img" aria-label="Black and white figure photograph for body procedures"><span class="feature__label">Body</span></div>
      <p class="feature__text">Contouring options that restore shape and balance, planned carefully around your own goals.</p>
      <p class="feature__more">Learn More ›</p>
    </article>
    <article class="feature">
      <div class="feature__photo" role="img" aria-label="Black and white figure photograph for breast procedures"><span class="feature__label">Breast</span></div>
      <p class="feature__text">Augmentation, lift and reduction options guided by experience and a natural aesthetic.</p>
      <p class="feature__more">Learn More ›</p>
    </article>
  </div>

  <div class="about">
    <div>
      <div class="about__photo" role="img" aria-label="Black and white portrait photograph of a woman"></div>
      <div class="dots"><span></span><span></span><span></span></div>
    </div>
    <div>
      <h2 class="about__title">Harbourline Cosmetic Institute</h2>
      <p class="about__sub">Your future looks beautiful</p>
      <p class="about__text">Our surgeons bring years of training and a gentle approach to every consultation, helping you feel informed and at ease before any decision.</p>
      <p class="about__text">From first visit to full recovery, our team supports you with clear advice, modern techniques and honest results.</p>
    </div>
  </div>

  <footer class="site-footer">
    <div class="footer-cols">
      <div class="footer-col"><h4>FACE</h4><ul><li>Facelift</li><li>Eyelid Surgery</li><li>Brow Lift Surgery</li><li>Rhinoplasty Surgery</li><li>Otoplasty Surgery</li><li>Laser Resurfacing</li><li>Chin Enlargement</li></ul></div>
      <div class="footer-col"><h4>BODY</h4><ul><li>Tummy Tuck</li><li>Liposuction</li><li>Arm Lift</li></ul></div>
      <div class="footer-col"><h4>BREAST</h4><ul><li>Breast Augmentation</li><li>Breast Reduction</li><li>Breast Lift</li><li>Breast Reconstruction</li></ul></div>
      <div class="footer-col footer-col--updates"><h4>UPDATES</h4><p>New patient guides are now online for every procedure. 2 minutes ago</p><p>Our clinic hours extend this month. 15 minutes ago</p></div>
      <div class="footer-col"><h4>GALLERY</h4><div class="gallery-grid" role="img" aria-label="Grid of small gallery photographs"><span></span><span></span><span></span><span></span><span></span><span></span><span></span><span></span></div></div>
    </div>
    <div class="footer-bar">
      <span>© Harbourline Cosmetic Institute. All rights reserved.</span>
      <div class="social"><span></span><span></span><span></span><span></span></div>
    </div>
  </footer>
</section>

</body>
</html>
```